Australian Consultant Pharmacist Business Needs A3 Flyer for Medical Centre

Our business has just secured a deal in a medical centre to offer our consulting services. We have installed our software on the doctors computers and would like to have an A3 flyer to put on their walls to remind them about our services and explain very briefly how to use our simple software.

We would like the flyer to be vibrant and very simple whilst conveying our message of improving patient health outcomes and illustrating how to use our software and service.

We provide Home Medicine Reviews (HMR) for General Practitioners (GP) at medical centres.

There are 3 pathways for a GP to use our service, all resulting in the same outcome.

The outcome is the Dr sends us a referral for a HMR for their patient. In turn they receive a report back after we have performed the HMR.

Pathways
1.
-GP Opens Patient File in medical prescribing software
-If patient is eligible for a HMR, an alert will pop up in bottom right hand corner (approx 30 seconds)
- Click Send Referral
- New page opens, select reason for referral ie. several medicines
- Press Send - referral is sent electronically to Pharmacist

2.
No alert pops up but GP still wants to refer.
Right click RX Notify program - RX Notify program is identified by the bell shape icon in the bottom right side of the desktop tray next to the time.
Click refer current patient - this will refer the patient currently open on the GP prescribing software

3. GP would like to send HMR Referal via Fax.
Fax number 03 9172 3408

I have attached some examples of how the software and service works, including screen shots and some power points. I would like to use these as ideas for our A3 Flyer.

Good Luck!

Target Market(s)

Doctors

Industry/Entity Type

Health Service

Colors
f37122
0455a3
3176b5
33a6d7
f68d4c

Requirements
Must have
• Our company name - Brightpath Care HMR
• Our email brightpathcarehmr@mailvista.example
• our fax number
• the 3 ways to use our service and how
• prefer images and short keyword descriptions
• convey idea of improving patient health
• ensure our service comes accross as simple and effecient
Nice to have
• images, vibrant,
Should not have
• lengthy descriptions

```html
<!DOCTYPE html>
<html lang="en">
<head>
<meta charset="utf-8">
<title>How To Use RX Notify – Brightpath Care HMR</title>
<link rel="stylesheet" href="https://fonts.googleapis.com/css2?family=Roboto+Condensed:ital,wght@0,700;1,400;1,500;1,700&display=swap">
<style>
  :root {
    --navy: #262264;
    --orange: #f0582a;
    --band-dark: #58585a;
    --band-light: #8b8b8d;
    --white: #ffffff;
    --screen-grey: #d6d6d8;
    --screen-blue: #3f68b4;
  }
  * { margin: 0; padding: 0; box-sizing: border-box; }
  html, body { width: 877px; height: 1200px; overflow: hidden; background: var(--navy); }
  .flyer {
    position: relative; width: 877px; height: 1200px; overflow: hidden;
    background: var(--navy);
    font-family: "Roboto Condensed", "Arial Narrow", sans-serif;
  }
  .title {
    position: absolute; left: 226px; top: 28px;
    color: var(--orange); font-size: 58px; font-style: italic; font-weight: 700;
    letter-spacing: 0.5px; white-space: nowrap;
  }
  .band {
    position: absolute; left: 110px; right: 0;
    background: linear-gradient(90deg, var(--band-dark) 0%, #6c6c6e 45%, var(--band-light) 100%);
  }
  .band--one { top: 109px; height: 286px; }
  .band--two { top: 418px; height: 285px; }
  .band--three { top: 729px; height: 284px; }
  .step-numbers { position: absolute; left: 0; top: 0; width: 877px; height: 1200px; pointer-events: none; }
  .step-text {
    position: absolute; left: 251px; color: var(--white);
    font-size: 14.5px; font-style: italic; font-weight: 500; line-height: 19.5px; white-space: nowrap;
  }
  .step-text--fax { left: 270px; width: 280px; text-align: center; }
  .fax-number { font-size: 25px; font-weight: 700; line-height: 30px; }
  .shot {
    position: absolute; box-shadow: 4px 5px 8px rgba(0,0,0,0.45);
  }
  .shot--alert { left: 641px; top: 136px; width: 209px; height: 109px; background: linear-gradient(180deg, #e2e2e4, #c9c9cc); }
  .shot--form-a { left: 641px; top: 264px; width: 209px; height: 93px; background: linear-gradient(180deg, #e9e9eb, #cfcfd2); }
  .shot--tray { left: 639px; top: 472px; width: 214px; height: 74px; background: linear-gradient(180deg, var(--screen-blue) 0%, #4a74be 78%, #bdbdc0 78%, #a9a9ac 100%); }
  .shot--form-b { left: 639px; top: 563px; width: 214px; height: 94px; background: linear-gradient(180deg, #e9e9eb, #cfcfd2); }
  .photo--fax { left: 636px; top: 803px; width: 214px; height: 117px; background: linear-gradient(135deg, #5a4e55 0%, #8c7f86 50%, #cfcad0 100%); }
  .photo--consult { left: 612px; top: 1037px; width: 217px; height: 140px; background: linear-gradient(135deg, #a98f6e 0%, #e3ddd2 50%, #8aa0b8 100%); }
  .brand {
    position: absolute; left: 34px; top: 1020px;
    color: var(--orange); font-size: 58px; font-style: italic; font-weight: 700; white-space: nowrap;
  }
  .contact {
    position: absolute; left: 36px; top: 1110px;
    color: var(--orange); font-size: 21px; font-style: italic; font-weight: 700; line-height: 28px; white-space: nowrap;
  }
</style>
</head>
<body>
<main class="flyer">
  <h1 class="title">How To Use RX Notify</h1>

  <div class="band band--one"></div>
  <div class="band band--two"></div>
  <div class="band band--three"></div>

  <svg class="step-numbers" viewBox="0 0 877 1200" aria-hidden="true">
    <g fill="var(--orange)" font-family="Roboto Condensed, Arial Narrow, sans-serif" font-weight="700">
      <text x="30" y="397" font-size="420" textLength="170" lengthAdjust="spacingAndGlyphs" font-style="italic">1</text>
      <text x="-4" y="708" font-size="420" textLength="224" lengthAdjust="spacingAndGlyphs">2</text>
      <text x="-4" y="1025" font-size="430" textLength="218" lengthAdjust="spacingAndGlyphs">3</text>
    </g>
  </svg>

  <section class="step-text" style="top:138px">
    <p>GP Opens Patient File in medical prescribing software</p>
    <p style="margin-top:15px">If patient is eligible for a HMR, an alert will pop up in<br>bottom right hand corner (approx 30 seconds)</p>
    <p style="margin-top:15px">Click Send Referral</p>
    <p style="margin-top:30px">New page opens, select reason<br>for referral ie. several medicines</p>
    <p style="margin-top:19px">Press Send - referral is sent electronically to Pharmacist</p>
  </section>
  <div class="shot shot--alert" role="img" aria-label="Screenshot of the RX Notify pop-up alert with Send Referral button"></div>
  <div class="shot shot--form-a" role="img" aria-label="Screenshot of the referral form for selecting a reason"></div>

  <section class="step-text" style="top:469px">
    <p>No alert pops up but GP still wants to refer.</p>
    <p style="margin-top:35px">Right click RX Notify program - RX Notify<br>program is identified by the bell shape icon in the<br>bottom right side of the desktoptray next to the time.</p>
    <p style="margin-top:31px">Click refer current patient - this will refer the patient<br>currently open on the GP prescribing software</p>
  </section>
  <div class="shot shot--tray" role="img" aria-label="Screenshot of the desktop tray showing the bell icon next to the clock"></div>
  <div class="shot shot--form-b" role="img" aria-label="Screenshot of the refer current patient form"></div>

  <section class="step-text step-text--fax" style="top:843px">
    <p>GP would like to send HMR Referal via Fax.</p>
    <p class="fax-number" style="margin-top:6px">Fax number 03 9172 3408</p>
  </section>
  <div class="shot photo--fax" role="img" aria-label="Photo of hands sending a document on a fax machine"></div>

  <p class="brand">Brightpath Care HMR</p>
  <p class="contact">brightpathcarehmr@mailvista.example<br>Fax number 03 9172 3408</p>
  <div class="shot photo--consult" role="img" aria-label="Photo of a pharmacist talking with an older couple in a pharmacy"></div>
</main>
</body>
</html>
```